Real Estate Listing Signs for standard Yard arms

I need real estate listing signs done, for the standard sized sign to be hung beneath a white yard arm. To match existing logo. Information to be included:
-Logo
-Business name
-Phone number
-Dorran Fitch Tundra Circle & Dorran Fitch realty logos (smaller print)

Colors to be Red and anywhere in the gray scale between black and white, or a combination of those.

Target Market(s)

Drive by visuals

Industry/Entity Type

Real Estate Agent

Colors

Designer to choose only greyscale colors for use in the design.

Requirements
Must have
• My Logo and business name in same/similar font to whats provided, the DF tundra circle logo (small on bottom or corner somewhere), My phone number, and a decent amount of red coloration on the sign.

```html
<!DOCTYPE html>
<html lang="en">
<head>
<meta charset="utf-8">
<title>Brannock Realty – Yard Sign</title>
<link rel="stylesheet" href="https://fonts.googleapis.com/css2?family=Cinzel:wght@600;700;800&family=Oswald:wght@400;500&family=Poppins:wght@600&display=swap">
<style>
  :root {
    --backdrop: #a3a1a2;
    --sign-white: #ffffff;
    --pattern-light: #f4f4f4;
    --pattern-mid: #dcdcdc;
    --brand-red: #c1121f;
    --ink: #1b1b1b;
    --band-black: #231f20;
    --band-text: #ffffff;
  }
  html, body {
    margin: 0;
    width: 1200px;
    height: 1200px;
    overflow: hidden;
    background: var(--backdrop);
  }
  .yard-sign {
    position: absolute;
    left: 50px;
    top: 188px;
    width: 1100px;
    height: 824px;
    display: block;
  }
  .brand-name { font-family: "Cinzel", serif; font-weight: 700; fill: var(--ink); }
  .agent-name { font-family: "Cinzel", serif; font-weight: 800; fill: var(--brand-red); }
  .contact-phone { font-family: "Poppins", sans-serif; font-weight: 600; fill: var(--ink); }
  .contact-email { font-family: "Cinzel", serif; font-weight: 700; fill: var(--ink); }
  .contact-email .at-sign { font-family: "Poppins", sans-serif; font-weight: 600; }
  .brokerage-name { font-family: "Oswald", sans-serif; font-weight: 500; fill: var(--band-text); }
  .brokerage-sub { font-family: "Oswald", sans-serif; font-weight: 400; fill: var(--band-text); }
  .office-notice { font-family: "Cinzel", serif; font-weight: 700; fill: var(--band-text); }
</style>
</head>
<body>
<svg class="yard-sign" viewBox="0 0 1208 905" xmlns="http://www.w3.org/2000/svg">
  <defs>
    <linearGradient id="texture-fade" x1="0" y1="0" x2="1" y2="0">
      <stop offset="0" stop-color="#dcdcdc"/>
      <stop offset="0.45" stop-color="#f4f4f4"/>
      <stop offset="0.75" stop-color="#ffffff"/>
    </linearGradient>
  </defs>

  <rect class="sign-face" width="1208" height="777" fill="var(--sign-white)"/>
  <g role="img" aria-label="Soft grey halftone and diamond texture background">
    <rect width="900" height="777" fill="url(#texture-fade)"/>
  </g>

  <rect class="brand-mark" x="566" y="122" width="76" height="76" fill="var(--brand-red)"/>
  <text class="brand-name" x="604" y="363" text-anchor="middle" font-size="64" textLength="630" lengthAdjust="spacingAndGlyphs">BRANNOCK REALTY</text>

  <text class="agent-name" x="604" y="545" text-anchor="middle" font-size="92" textLength="1043" lengthAdjust="spacingAndGlyphs">JORDAN BRANNOCK</text>

  <g class="icon-phone" fill="var(--brand-red)">
    <path d="M93 584c-6 2-10 8-9 15 3 10 9 18 17 24 6 4 13 2 16-4l-7-8-5 3c-4-3-8-8-10-13l4-4-6-13z"/>
    <path d="M106 584a14 14 0 0 1 13 13" fill="none" stroke="var(--brand-red)" stroke-width="3"/>
    <path d="M106 577a21 21 0 0 1 20 20" fill="none" stroke="var(--brand-red)" stroke-width="3"/>
  </g>
  <text class="contact-phone" x="141" y="615" font-size="44" textLength="344" lengthAdjust="spacingAndGlyphs">907-555-0148</text>

  <line class="contact-divider" x1="509" y1="575" x2="509" y2="628" stroke="var(--ink)" stroke-width="2"/>

  <g class="icon-mail">
    <rect x="533" y="587" width="42" height="30" fill="var(--brand-red)"/>
    <path d="M533 587l21 16 21-16M533 617l15-14M575 617l-15-14" fill="none" stroke="var(--sign-white)" stroke-width="2.5"/>
  </g>
  <text class="contact-email" x="593" y="617" font-size="38" textLength="533" lengthAdjust="spacingAndGlyphs">JBRANNOCK<tspan class="at-sign">@</tspan>MAILBOX.COM</text>

  <rect class="band-brokerage" x="0" y="777" width="604" height="128" fill="var(--band-black)"/>
  <text class="brokerage-name" x="141" y="850" font-size="42" textLength="354" lengthAdjust="spacingAndGlyphs">DF TUNDRA CIRCLE</text>
  <text class="brokerage-sub" x="141" y="876" font-size="20" textLength="242" lengthAdjust="spacingAndGlyphs">DORRAN FITCH REALTY</text>

  <rect class="band-notice" x="604" y="777" width="604" height="128" fill="var(--brand-red)"/>
  <text class="office-notice" x="906" y="832" text-anchor="middle" font-size="27" textLength="466" lengthAdjust="spacingAndGlyphs">EACH OFFICE INDEPENDENTLY</text>
  <text class="office-notice" x="906" y="864" text-anchor="middle" font-size="27" textLength="366" lengthAdjust="spacingAndGlyphs">OWNED AND OPERATED</text>
</svg>
</body>
</html>
```